We need a business card design for a new brand within our existing financial marketing business. Our new brand is www.qalvenport.co.uk

We attach various logo files - please use the version that will produce the sharpest image on the business card.

We are flexible about shape of card etc. Please think outside the box as to what goes on front and what goes on back of the card.

The card needs to be corporate, but really catch the eye ( e.g. premium translucent cards on plastic etc or metal cards or shiny surface etc )

We want to be able to amend the card (once the design has been agreed ) to add additional staff details, but the text to go on it will be generic

Details to go on card ( for the first generic one) are fairly minimal as we don't like cluttered business cards:-

Owen Tagget
Managing Director

Mobile: 07852 418 207
Email: o.tagget@qalvenport.co.uk

Financial

```html
<!DOCTYPE html>
<html lang="en">
<head>
<meta charset="utf-8">
<title>Qalvenport – Business Card</title>
<link rel="stylesheet" href="https://fonts.googleapis.com/css2?family=Montserrat:wght@700&family=Raleway:wght@300;400;500&display=swap">
<style>
  :root {
    --page-bg: #e6e6e6;
    --card-dark: #262525;
    --card-dark-edge: #1b1a1a;
    --card-light: #f7f7f6;
    --brand-yellow: #c7ae17;
    --brand-blue: #3e6cb4;
    --text-light: #f2f2f2;
  }
  * { margin: 0; padding: 0; box-sizing: border-box; }
  html, body {
    width: 1200px; height: 750px; overflow: hidden;
    background: var(--page-bg);
  }
  .canvas {
    position: relative; width: 1200px; height: 750px;
    display: flex; align-items: center; justify-content: center; gap: 60px;
    background: radial-gradient(ellipse at 50% 40%, #f0f0f0 0%, var(--page-bg) 70%);
  }
  .card {
    position: relative; width: 500px; height: 290px;
    border-radius: 26px; overflow: hidden;
    box-shadow: 0 6px 18px rgba(0,0,0,0.18);
  }

  /* Front: dark side */
  .card--front {
    background: linear-gradient(160deg, #343333 0%, var(--card-dark) 45%, var(--card-dark-edge) 100%);
    display: flex; align-items: center; justify-content: center;
  }
  .brand--front {
    display: flex; align-items: center; gap: 16px;
    font-family: "Raleway", sans-serif; font-weight: 300;
    font-size: 64px; letter-spacing: 1px; color: var(--text-light);
  }
  .brand-mark {
    width: 46px; height: 46px; background: var(--brand-yellow); flex: none;
  }

  /* Back: light side */
  .card--back { background: var(--card-light); }
  .brand--back {
    position: absolute; top: 42px; left: 0; right: 0;
    display: flex; align-items: center; justify-content: center; gap: 12px;
    font-family: "Raleway", sans-serif; font-weight: 300;
    font-size: 44px; letter-spacing: 0.5px; color: var(--brand-blue);
  }
  .brand--back .brand-mark { width: 32px; height: 32px; }

  .person {
    position: absolute; left: 34px; bottom: 68px;
  }
  .person-name {
    font-family: "Montserrat", sans-serif; font-weight: 700;
    font-size: 26px; color: var(--brand-blue); line-height: 1.1;
  }
  .person-role {
    font-family: "Raleway", sans-serif; font-weight: 500;
    font-variant: small-caps; font-size: 16px; letter-spacing: 0.5px;
    color: var(--brand-yellow);
  }

  .contact {
    position: absolute; right: 30px; top: 128px;
    list-style: none; display: flex; flex-direction: column; gap: 7px;
    font-family: "Raleway", sans-serif; font-weight: 400;
    font-size: 14px; color: var(--brand-yellow);
  }
  .contact-item { display: flex; align-items: center; gap: 8px; }
  .contact-icon { width: 15px; height: 15px; flex: none; }

  .edge-band {
    position: absolute; left: 0; right: 0; bottom: 0; height: 16px; display: flex;
  }
  .edge-band__yellow { flex: 0 0 58%; background: var(--brand-yellow); }
  .edge-band__blue { flex: 1; background: var(--brand-blue); }
</style>
</head>
<body>
<main class="canvas">
  <section class="card card--front" aria-label="Card front">
    <div class="brand brand--front">
      <span class="brand-mark" aria-hidden="true"></span>
      <span class="brand-name">qalvenport</span>
    </div>
  </section>

  <section class="card card--back" aria-label="Card back">
    <div class="brand brand--back">
      <span class="brand-mark" aria-hidden="true"></span>
      <span class="brand-name">qalvenport</span>
    </div>

    <ul class="contact">
      <li class="contact-item">
        <svg class="contact-icon" viewBox="0 0 16 16" aria-hidden="true">
          <circle cx="8" cy="8" r="8" fill="#3e6cb4"/>
          <path d="M5.2 4.2l1.4-.4.8 2-1 .7c.4.9 1.1 1.6 2 2l.7-1 2 .8-.4 1.4c-3 .1-5.6-2.5-5.5-5.5z" fill="#fff"/>
        </svg>
        <span>07852 418 207</span>
      </li>
      <li class="contact-item">
        <svg class="contact-icon" viewBox="0 0 16 16" aria-hidden="true">
          <circle cx="8" cy="8" r="8" fill="#3e6cb4"/>
          <rect x="4" y="5" width="8" height="6" rx="0.6" fill="#fff"/>
          <path d="M4.3 5.3L8 8.3l3.7-3" fill="none" stroke="#3e6cb4" stroke-width="0.9"/>
        </svg>
        <span>o.tagget@qalvenport.co.uk</span>
      </li>
      <li class="contact-item">
        <svg class="contact-icon" viewBox="0 0 16 16" aria-hidden="true">
          <circle cx="8" cy="8" r="8" fill="#3e6cb4"/>
          <path d="M6.5 4l4.5 4.5-2.1.2 1.2 2.6-1 .5-1.2-2.6L6.5 10.7z" fill="#fff"/>
        </svg>
        <span>www.qalvenport.co.uk</span>
      </li>
    </ul>

    <div class="person">
      <p class="person-name">Owen Tagget</p>
      <p class="person-role">Managing Director</p>
    </div>

    <div class="edge-band" aria-hidden="true">
      <span class="edge-band__yellow"></span>
      <span class="edge-band__blue"></span>
    </div>
  </section>
</main>
</body>
</html>
```